Lumen Jewellers
Grace at every pace™
Lumen Jewellers -
Creative Brief
Professional
Martin Kasperak and Lionel Kasperak make it saparate
4715 Harlow Ridge Way Suite B, Carlsbad CA 92011
not yet will tell you soon
Martin@lumenjewellers-example.com
www.lumenjewellers-example.com
the businesss cards has to be as elegant as possible but not to busy. make the corners rounded. Mine CEO Martin Kasperak Master Goldsmith & Certified Diamond setter. email: martin@lumenjewellers-example.com I need one for my brother. CEO Lionel Kasperak, PKT Fine Jewelry Designer & Custom specialist email: lionel@lumenjewellers-example.com Our address: 4715 Harlow Ridge Way Suite B, Carlsbad CA 92011 Phone: Not set up yet Website: www.lumenjewellers-example.com very important some where on the business card it should say in very small print: Lumen Creations.
Business card include this ring (doesn't have to) i just want to see how it looks. Front Page http://pix4.snapvault-example.net/pix4/5182/ring004926.jpg

```html
<!DOCTYPE html>
<html lang="en">
<head>
<meta charset="utf-8">
<title>Lumen Jewellers – Business Card</title>
<link rel="stylesheet" href="https://fonts.googleapis.com/css2?family=Questrial&family=Arimo:wght@400;700&display=swap">
<style>
  :root {
    --backdrop: #4a3328;
    --card: #0b0b0b;
    --card-edge: #1d1d1d;
    --white: #f2f2f2;
    --grey: #9a9a9a;
    --dim: #555555;
    --gold: #e0a126;
    --photo-light: #d4d4d4;
    --photo-dark: #3e3e3e;
  }
  * { margin: 0; padding: 0; box-sizing: border-box; }
  html, body { width: 1200px; height: 927px; overflow: hidden; }
  body {
    background: var(--backdrop);
    position: relative;
    font-family: "Arimo", Arial, sans-serif;
    color: var(--white);
  }
  .card {
    position: absolute;
    width: 645px;
    height: 360px;
    background: linear-gradient(160deg, var(--card-edge), var(--card) 55%);
    border-radius: 28px;
    box-shadow: 0 14px 30px rgba(0,0,0,.45);
    overflow: hidden;
  }
  .card p, .card address { position: absolute; white-space: nowrap; font-style: normal; }
  .card-front { left: 88px; top: 70px; }
  .card-back { left: 475px; top: 493px; }

  /* front */
  .brand-mark {
    position: absolute; left: 150px; top: 26px;
    width: 64px; height: 64px; border: 3px solid var(--white); border-radius: 50%;
  }
  .brand-name {
    left: 22px; top: 122px;
    font-family: "Questrial", "Century Gothic", sans-serif;
    font-size: 46px; line-height: 1; letter-spacing: -.5px; color: var(--white);
  }
  .tagline {
    left: 150px; top: 176px;
    font-size: 10px; font-weight: 700; letter-spacing: 1.2px; text-transform: uppercase;
  }
  .services {
    left: 22px; top: 200px;
    font-size: 11px; color: var(--gold); word-spacing: 2px;
  }
  .owner-role { left: 22px; top: 234px; font-size: 13px; color: var(--gold); }
  .owner-name {
    left: 22px; top: 250px;
    font-family: "Questrial", sans-serif; font-size: 22px; color: var(--gold);
  }
  .owner-title { left: 22px; top: 282px; font-size: 13px; color: var(--white); }
  .owner-email { left: 22px; top: 316px; font-size: 16px; color: var(--gold); }

  .address {
    left: 412px; top: 20px;
    font-size: 13px; line-height: 20px; color: var(--white);
  }
  .affiliations {
    position: absolute; left: 478px; top: 282px;
    display: flex; gap: 12px; align-items: center;
  }
  .badge-square { width: 14px; height: 20px; background: var(--white); }
  .badge-circle { width: 20px; height: 20px; border-radius: 50%; background: var(--white); }
  .badge-oval { width: 30px; height: 16px; border-radius: 8px; background: var(--white); }
  .imprint { left: 492px; top: 324px; font-size: 11px; color: var(--grey); }

  /* back */
  .ring-photo {
    position: absolute; left: 42px; top: 52px;
    width: 233px; height: 243px; border-radius: 20px;
    background: radial-gradient(circle at 45% 40%, var(--photo-light), var(--photo-dark) 70%, #1e1e1e);
  }
  .back-brand {
    left: 400px; top: 190px;
    font-family: "Questrial", sans-serif; font-size: 20px; color: var(--dim);
  }
  .back-web { left: 312px; top: 290px; font-size: 20px; color: var(--white); }
</style>
</head>
<body>
  <section class="card card-front">
    <span class="brand-mark"></span>
    <p class="brand-name">Lumen Jewellers</p>
    <p class="tagline">Grace at every pace™</p>
    <p class="services">Repair . Design Gems . Watches . Appraisal</p>
    <p class="owner-role">OWNER</p>
    <p class="owner-name">Martin Kasperak</p>
    <p class="owner-title">Master Goldsmith &amp; Certified Diamond setter</p>
    <p class="owner-email">email: martin@lumenjewellers-example.com</p>
    <address class="address">
      4715 Harlow Ridge Way<br>
      Suite B<br>
      Carlsbad CA 92011<br>
      P : 000.123.4567<br>
      www.lumenjewellers-example.com
    </address>
    <div class="affiliations">
      <span class="badge-square"></span>
      <span class="badge-circle"></span>
      <span class="badge-oval"></span>
    </div>
    <p class="imprint">Lumen Creations</p>
  </section>

  <section class="card card-back">
    <div class="ring-photo" role="img" aria-label="Photograph of a gold and silver flower ring with a dark pearl"></div>
    <p class="back-brand">Lumen Jewellers</p>
    <p class="back-web">www.lumenjewellers-example.com</p>
  </section>
</body>
</html>
```